Looking for a creative label design for our retail coffee bags

We are a coffee manufacturer (coffee roaster) looking to re-brand our retail label for our coffee bags. Our main coffee blend that we sell is our Harborline Velvet Blend. You can use this name when creating the label. We are going for a look that represents our company as a coffee roaster. Please reference our website (www.brindlemugworks.com) and our Facebook page to learn more about our company and to give you more inspiration on creating this design.

Target Market(s)

Retail customers/grocery stores

Industry/Entity Type

Manufacturer

Requirements
Must have
• The size of the label has to be 3" width x 4" height

Logo must be Black
Nice to have
• We currently incorporate a color on our labels for each blend. For example, Harborline Velvet Blend (royal blue), Decaffeinated Blend (red), Breakfast Blend (green), Flavored coffees (gold).

Rustic/vintage style

```html
<!DOCTYPE html>
<html lang="en">
<head>
<meta charset="utf-8">
<title>Brindle Mugworks – Retail Bag Labels</title>
<link rel="stylesheet" href="https://fonts.googleapis.com/css2?family=Oswald:wght@500;600&family=Lobster&family=Roboto+Condensed:wght@400&display=swap">
<style>
  :root {
    --canvas: #ffffff;
    --burlap: #d2ad84;
    --burlap-edge: #c19a70;
    --ink: #1b1b1b;
    --paper: #ffffff;
    --decaf-green: #2aa844;
    --decaf-red: #cf3b27;
    --sketch-light: #cdb08e;
    --sketch-dark: #8f7659;
  }
  * { box-sizing: border-box; margin: 0; padding: 0; }
  html, body { width: 1200px; height: 840px; overflow: hidden; }
  body {
    background: var(--canvas);
    font-family: "Roboto Condensed", Arial, sans-serif;
    position: relative;
  }
  .label {
    position: absolute;
    top: 150px;
    width: 420px;
    height: 560px;
    background: var(--burlap);
    border: 1px solid var(--burlap-edge);
  }
  .label--green { left: 100px; --blend: var(--decaf-green); }
  .label--red { left: 680px; --blend: var(--decaf-red); }

  .brand-mark {
    position: absolute;
    left: 140px;
    top: 60px;
    width: 140px;
    height: 140px;
    border-radius: 50%;
    background: var(--ink);
    border: 2px solid #3a3a3a;
    display: flex;
    align-items: center;
    justify-content: center;
    text-align: center;
  }
  .brand-name {
    font-family: "Oswald", Arial, sans-serif;
    font-weight: 600;
    font-size: 24px;
    line-height: 1.05;
    color: var(--paper);
    text-transform: uppercase;
  }
  .brand-tagline {
    position: absolute;
    top: 206px;
    left: 0;
    width: 100%;
    text-align: center;
    font-size: 7px;
    letter-spacing: 0.4px;
    color: var(--ink);
  }

  .blend-banner {
    position: absolute;
    left: 45px;
    top: 232px;
    width: 330px;
    height: 56px;
    display: flex;
  }
  .blend-banner__roast {
    width: 74px;
    background: var(--ink);
    color: var(--paper);
    font-family: "Lobster", cursive;
    font-size: 16px;
    line-height: 1.05;
    display: flex;
    align-items: center;
    justify-content: center;
    text-align: center;
  }
  .blend-banner__name {
    flex: 1;
    background: var(--blend);
    color: var(--paper);
    font-family: "Oswald", Arial, sans-serif;
    padding: 5px 0 0 6px;
    text-transform: uppercase;
    line-height: 1;
  }
  .blend-banner__origin { font-size: 23px; font-weight: 600; display: block; }
  .blend-banner__type { font-size: 13px; font-weight: 500; display: block; margin-top: 2px; }

  .roasting-scene {
    position: absolute;
    left: 80px;
    top: 306px;
    width: 260px;
    height: 116px;
    border-radius: 50% 50% 12px 12px / 30% 30% 12px 12px;
    background: radial-gradient(ellipse at 50% 60%, var(--sketch-dark) 0%, var(--sketch-light) 75%, var(--burlap) 100%);
  }
  .net-weight {
    position: absolute;
    top: 430px;
    right: 95px;
    font-size: 8px;
    color: var(--ink);
  }
</style>
</head>
<body>

<section class="label label--green">
  <div class="brand-mark"><span class="brand-name">Brindle<br>Mugworks</span></div>
  <p class="brand-tagline">Proudly roasted in small batches since day one</p>
  <div class="blend-banner">
    <div class="blend-banner__roast">Fresh<br>Roasted</div>
    <div class="blend-banner__name">
      <span class="blend-banner__origin">Colombian</span>
      <span class="blend-banner__type">Decaffeinated Blend</span>
    </div>
  </div>
  <div class="roasting-scene" role="img" aria-label="Vintage engraved sketch of a coffee bean sack, hand grinder, cezve pot, cup and scattered beans"></div>
  <p class="net-weight">16 oz. | Net Wt. 500g</p>
</section>

<section class="label label--red">
  <div class="brand-mark"><span class="brand-name">Brindle<br>Mugworks</span></div>
  <p class="brand-tagline">Proudly roasted in small batches since day one</p>
  <div class="blend-banner">
    <div class="blend-banner__roast">Fresh<br>Roasted</div>
    <div class="blend-banner__name">
      <span class="blend-banner__origin">Colombian</span>
      <span class="blend-banner__type">Decaffeinated Blend</span>
    </div>
  </div>
  <div class="roasting-scene" role="img" aria-label="Vintage engraved sketch of a coffee bean sack, hand grinder, cezve pot, cup and scattered beans"></div>
  <p class="net-weight">16 oz. | Net Wt. 500g</p>
</section>

</body>
</html>
```